Need a business card for a Construction and Remodeling company.
Our company logo is the fleur de lis design as thats the family crust that we use on our logos.
Heres the info it needs:

Brackmore Construction & Remodeling, LLC
Renovations * Restorations

Elwin R. Brackmore
845 North Quarry Road
Fernwick Vermont 05847
(203) 555.0182
CT LIC/REG: 418257

home owners, customers

```html
<!DOCTYPE html>
<html lang="en">
<head>
<meta charset="utf-8">
<title>Brackmore Construction &amp; Remodeling — Business Card</title>
<link rel="stylesheet" href="https://fonts.googleapis.com/css2?family=Cinzel:wght@600&family=Crimson+Text:ital,wght@0,700;1,400&family=Poppins:wght@300;400&display=swap">
<style>
  :root {
    --backdrop: #e8e5e1;
    --card-white: #ffffff;
    --band-grey: #5a5c5b;
    --ink-dark: #4a4a4a;
    --ink-tagline: #9b9b9b;
    --mark-grey: #cfcfcf;
    --band-text: #ffffff;
  }
  * { box-sizing: border-box; margin: 0; padding: 0; }
  html, body {
    width: 1200px;
    height: 1200px;
    overflow: hidden;
    background: var(--backdrop);
  }
  body {
    display: flex;
    align-items: center;
    justify-content: center;
  }
  .business-card {
    width: 560px;
    height: 980px;
    background: var(--card-white);
    display: flex;
    flex-direction: column;
    box-shadow: 0 6px 24px rgba(0,0,0,0.12);
  }
  .card-top {
    flex: 0 0 620px;
    display: flex;
    flex-direction: column;
    align-items: center;
    padding-top: 56px;
  }
  .tagline {
    font-family: "Crimson Text", Georgia, serif;
    font-style: italic;
    font-weight: 400;
    font-size: 33px;
    color: var(--ink-tagline);
    letter-spacing: 0.2px;
    white-space: nowrap;
  }
  .brand {
    margin-top: 44px;
    display: flex;
    flex-direction: column;
    align-items: center;
  }
  .brand-dot {
    width: 190px;
    height: 190px;
    border-radius: 50%;
    background: var(--mark-grey);
  }
  .brand-name {
    margin-top: 44px;
    font-family: "Cinzel", "Times New Roman", serif;
    font-weight: 600;
    color: var(--ink-dark);
    text-align: center;
    line-height: 1;
  }
  .brand-name .word {
    display: block;
    font-size: 62px;
    letter-spacing: 1px;
  }
  .brand-name .entity {
    display: block;
    margin-top: 16px;
    font-size: 19px;
    letter-spacing: 0.6px;
  }
  .card-band {
    flex: 1;
    background: var(--band-grey);
    color: var(--band-text);
    display: flex;
    flex-direction: column;
    align-items: center;
    padding-top: 34px;
    text-align: center;
  }
  .person-name {
    font-family: "Crimson Text", Georgia, serif;
    font-weight: 700;
    font-size: 43px;
    letter-spacing: 1px;
  }
  .address {
    margin-top: 8px;
    font-family: "Poppins", Arial, sans-serif;
    font-weight: 300;
    font-style: normal;
    font-size: 28px;
    line-height: 36px;
  }
  .license {
    margin-top: 44px;
    font-family: "Poppins", Arial, sans-serif;
    font-weight: 400;
    font-size: 14px;
    letter-spacing: 0.3px;
  }
</style>
</head>
<body>
  <article class="business-card">
    <section class="card-top">
      <p class="tagline">Renovations • Additions • Restorations</p>
      <div class="brand">
        <div class="brand-dot" aria-hidden="true"></div>
        <h1 class="brand-name">
          <span class="word">BRACKMORE</span>
          <span class="entity">CONSTRUCTION &amp; REMODELING, LLC</span>
        </h1>
      </div>
    </section>
    <section class="card-band">
      <h2 class="person-name">Elwin R. Brackmore</h2>
      <address class="address">
        845 North Quarry Road<br>
        Fernwick<br>
        Vermont 05847<br>
        (203) 555-0182
      </address>
      <p class="license">LIC/REG: 418257</p>
    </section>
  </article>
</body>
</html>
```